Modern Business Card For A Digital Advertising Company

I'll be print on the Tally Prints Velvet paper http://us.tallyprints-example.com/products/velvet/business-cards.html
Need's to be modern and use the color palette of the logo or gray scales. I think integrating the pixelation of the logo in to the card and having it wrap from one side to the other could be interesting. My company provides ad operations, web development, and number of other services to websites around the world. You can see my website at http://www.brightorbitads-example.com
Contact info on the card needs to have
Dana Welby
President
p.555.308.4127
dana@brightorbitads-example.com
http://www.brightorbitads-example.com
Doesn't necessarily need to be in that order
Target Market(s)
Website owners
Industry/Entity Type
Business
Look and feel
Each slider illustrates characteristics of the customer's brand and the style your logo design should communicate.

```html
<!DOCTYPE html>
<html lang="en">
<head>
<meta charset="utf-8">
<title>Bright Orbit Ads – Business Card</title>
<link rel="stylesheet" href="https://fonts.googleapis.com/css2?family=Oxanium:wght@500;600&family=Source+Sans+3:wght@400&display=swap">
<style>
  :root {
    --lime: #8dc63f;
    --ink: #111111;
    --white: #ffffff;
    --black: #000000;
    --frame: #9a9a9a;
    --label: #111111;
  }
  * { box-sizing: border-box; margin: 0; padding: 0; }
  html, body {
    width: 1200px; height: 1000px; overflow: hidden;
    background: var(--white);
  }
  .sheet { position: relative; width: 1200px; height: 1000px; }

  .card { position: absolute; overflow: hidden; font-family: "Oxanium", sans-serif; }
  .card--front {
    left: 210px; top: 181px; width: 368px; height: 639px;
    border: 2px solid var(--frame); background: var(--white);
  }
  .card--back {
    left: 627px; top: 182px; width: 363px; height: 636px;
    background: var(--black);
  }

  .brand {
    position: absolute; left: 0; width: 100%;
    display: flex; flex-direction: column; align-items: center; gap: 14px;
    color: var(--lime); font-weight: 600; text-transform: uppercase;
    text-align: center; line-height: 1.05; font-size: 30px; letter-spacing: 2px;
  }
  .brand__mark { width: 34px; height: 34px; background: var(--lime); }
  .card--front .brand { top: 64px; }
  .card--back .brand { top: 150px; }

  .contact-panel {
    position: absolute; left: 0; top: 269px; width: 100%; height: 368px;
    background: var(--lime); text-align: center;
  }
  .contact__name {
    position: absolute; top: 60px; width: 100%;
    font-size: 25px; font-weight: 500; letter-spacing: 2.5px; color: var(--ink);
  }
  .contact__role {
    position: absolute; top: 96px; width: 100%;
    font-size: 19px; font-weight: 500; letter-spacing: 1.5px; color: var(--white);
  }
  .contact__phone {
    position: absolute; top: 155px; width: 100%;
    font-size: 23px; font-weight: 500; letter-spacing: 2px; color: var(--ink);
  }
  .contact__email {
    position: absolute; top: 188px; width: 100%;
    font-size: 15px; font-weight: 500; letter-spacing: 1px; color: var(--ink);
  }
  .contact__prefix { color: var(--white); }

  .pixel-band { position: absolute; left: 2px; width: calc(100% - 4px); }
  .card--front .pixel-band {
    top: 287px; height: 76px;
    background: linear-gradient(to bottom, var(--lime), #e6f3d4 70%, #f7fbf1);
  }
  .card--back .pixel-band {
    left: 1px; top: 560px; height: 74px; width: calc(100% - 2px);
    background: linear-gradient(to bottom, var(--black), #7a7a7a 65%, #cfcfcf);
  }

  .site-url {
    position: absolute; top: 414px; width: 100%; text-align: center;
    color: var(--white); font-size: 19px; font-weight: 500; letter-spacing: 2.5px;
  }

  .side-label {
    position: absolute; font-family: "Source Sans 3", sans-serif;
    font-size: 31px; color: var(--label);
  }
  .side-label--front { left: 346px; top: 860px; }
  .side-label--back { left: 769px; top: 856px; }
</style>
</head>
<body>
<main class="sheet">
  <section class="card card--front" aria-label="Card front">
    <div class="brand">
      <span class="brand__mark" aria-hidden="true"></span>
      <span class="brand__name">Bright Orbit<br>Ads</span>
    </div>
    <div class="contact-panel">
      <p class="contact__name">DANA WELBY</p>
      <p class="contact__role">President</p>
      <p class="contact__phone"><span class="contact__prefix">P.</span>555.308.4127</p>
      <p class="contact__email"><span class="contact__prefix">E.</span>dana@brightorbitads-example.com</p>
      <div class="pixel-band" role="img" aria-label="Band of scattered white pixel squares rising from the bottom edge"></div>
    </div>
  </section>

  <section class="card card--back" aria-label="Card back">
    <div class="brand">
      <span class="brand__mark" aria-hidden="true"></span>
      <span class="brand__name">Bright Orbit<br>Ads</span>
    </div>
    <p class="site-url">brightorbitads-example.com</p>
    <div class="pixel-band" role="img" aria-label="Band of scattered white pixel squares rising from the bottom edge"></div>
  </section>

  <p class="side-label side-label--front">front</p>
  <p class="side-label side-label--back">back</p>
</main>
</body>
</html>
```